Kitchen manufaturer business card/logo design

I am a small kitchen manufacturing company that makes and installs all sorts of cabinetry.

The colours im looking to incorporate in the card are light/baby blue, white and black.

Incorporate 5 stars to show quality workmanship and product.

Looking for a modern classy design.
Updates

Hey guys, New idea. The logo should be made using HK in the most modern way possible as well as the full company name below it. Thanks.

Target Market(s)

Anyone with a home thats looking for a new cabinetry of any sort.

Industry/Entity Type

Business

Contact Information for Business Card

Harbor Kitchens
Ted Lowther
PH 0491 358 902
Email- harborkitchens@mailvane.example
ABN- 83 507 962 318
-Kitchens
-Vanities
-Laundries
-Media Units
-Studies
-Wardrobes
-3D Computer Designs

Requirements
Must have

• The front of the card must only have the company name.
The different types of cabinetry I do must be on the back of the card in point form but instead of using points use stars.
Nice to have
• Just think classy and quality

```html
<!DOCTYPE html>
<html lang="en">
<head>
<meta charset="utf-8">
<title>Harbor Kitchens – Business Card</title>
<link rel="stylesheet" href="https://fonts.googleapis.com/css2?family=Fira+Sans:wght@300;400;600&family=Yellowtail&display=swap">
<style>
  :root {
    --baby-blue: #8ccff0;
    --ink: #1f1d1d;
    --paper: #ffffff;
    --backdrop: #e8e5e1;
    --star: #ffffff;
  }
  * { box-sizing: border-box; margin: 0; padding: 0; }
  html, body { width: 1200px; height: 1000px; overflow: hidden; }
  body { background: var(--backdrop); position: relative; font-family: "Fira Sans", sans-serif; color: var(--ink); }

  .card {
    position: absolute; left: 225px; width: 750px; height: 453px;
    box-shadow: 0 2px 6px rgba(0,0,0,0.18);
  }
  .card-front { top: 32px; background: var(--baby-blue); display: flex; align-items: center; justify-content: center; }
  .brand-name { font-family: "Fira Sans", sans-serif; font-weight: 600; font-size: 58px; letter-spacing: 1px; color: var(--ink); }

  .card-back { top: 510px; background: var(--paper); }
  .services-band {
    position: absolute; left: 0; top: 0; width: 100%; height: 175px;
    background: var(--baby-blue);
    display: flex; flex-direction: column; align-items: center; justify-content: center; gap: 2px;
    padding-top: 4px;
  }
  .service-row { display: flex; gap: 34px; font-family: "Yellowtail", cursive; font-size: 35px; line-height: 41px; color: var(--ink); }
  .service::before { content: "★"; font-family: "Fira Sans", sans-serif; color: var(--star); font-size: 20px; margin-right: 4px; vertical-align: 5px; }

  .contact-name { position: absolute; top: 208px; width: 100%; text-align: center; font-weight: 600; font-size: 31px; letter-spacing: 0.5px; }
  .rule { position: absolute; left: 37px; width: 676px; height: 2px; background: var(--ink); }
  .rule-1 { top: 260px; } .rule-2 { top: 314px; } .rule-3 { top: 374px; }
  .contact-line { position: absolute; width: 100%; display: flex; justify-content: center; align-items: center; gap: 12px; font-weight: 300; font-size: 23px; }
  .contact-phone { top: 274px; } .contact-email { top: 332px; } .contact-abn { top: 390px; }
  .contact-line svg { width: 22px; height: 22px; fill: var(--baby-blue); }
  .abn-label { color: var(--baby-blue); font-weight: 400; }
</style>
</head>
<body>
  <section class="card card-front">
    <div class="brand-name">Harbor Kitchens</div>
  </section>

  <section class="card card-back">
    <div class="services-band">
      <div class="service-row"><span class="service">Kitchens</span><span class="service">Vanities</span><span class="service">Laundries</span></div>
      <div class="service-row"><span class="service">Media Units</span><span class="service">Studies</span><span class="service">Wardrobes</span></div>
      <div class="service-row"><span class="service">3D Computer Designs</span></div>
    </div>

    <div class="contact-name">Ted Lowther</div>
    <div class="rule rule-1"></div>
    <div class="contact-line contact-phone">
      <svg viewBox="0 0 24 24" aria-hidden="true"><path d="M6.6 10.8a15.1 15.1 0 0 0 6.6 6.6l2.2-2.2a1 1 0 0 1 1-.25 11.4 11.4 0 0 0 3.6.57 1 1 0 0 1 1 1V20a1 1 0 0 1-1 1A17 17 0 0 1 3 4a1 1 0 0 1 1-1h3.5a1 1 0 0 1 1 1c0 1.25.2 2.45.57 3.57a1 1 0 0 1-.25 1z"/></svg>
      <span>0491 358 902</span>
    </div>
    <div class="rule rule-2"></div>
    <div class="contact-line contact-email">
      <svg viewBox="0 0 24 24" aria-hidden="true"><path d="M2 6.5 12 13l10-6.5V19H2z"/><path d="M2 5h20l-10 6.5z"/></svg>
      <span>harborkitchens@mailvane.example</span>
    </div>
    <div class="rule rule-3"></div>
    <div class="contact-line contact-abn">
      <span class="abn-label">ABN</span><span>83 507 962 318</span>
    </div>
  </section>
</body>
</html>
```